Book Cover - For Best Selling Diet

Hi
Book cover required for a diet book being marketed to become a best seller
For best quality, image will be 2820 pixels on the shortest side and 4500 pixels on the longest side .
The book name : Bright Morning Plan
By Marisol Penhale
( will add in the extra text once we see design - top and bottom subtitle )
I do not want a photo of a person on the book.
PLEASE SEE " THE NINE STEP CORE" by Dale Whitcombe as an example of solid style and I also love Quiet Lantern for the font.
Branding Colours:
#F26432
#A4195C
#A7D8CC
Font that runs through our brand is : helvetica neue
This is for a book that will be marketed for #1 bestseller - So please only quality
designs that are designed in a unique style.
Thanks
Target Market(s)
Busy Working Mums, Affluent, 30+ .
Look and feel

```html
<!DOCTYPE html>
<html lang="en">
<head>
<meta charset="utf-8">
<title>Bright Morning Plan — Marisol Penhale</title>
<link rel="stylesheet" href="https://fonts.googleapis.com/css2?family=Inter+Tight:wght@200;300&family=Roboto+Condensed:wght@700&display=swap">
<style>
  :root {
    --orange: #ea5f28;
    --berry: #a2195b;
    --mint: #a7d8cc;
    --white: #ffffff;
    --title-font: "Inter Tight", "Helvetica Neue", Arial, sans-serif;
    --author-font: "Roboto Condensed", "Helvetica Neue", Arial, sans-serif;
  }
  html, body {
    margin: 0;
    padding: 0;
    width: 752px;
    height: 1200px;
    overflow: hidden;
    background: var(--orange);
  }
  .cover {
    position: relative;
    width: 752px;
    height: 1200px;
    background: var(--orange);
    overflow: hidden;
  }
  .figure-area {
    position: absolute;
    left: 150px;
    top: 0;
    width: 452px;
    height: 1200px;
    background: linear-gradient(to bottom,
      var(--white) 0px, var(--white) 196px,
      var(--berry) 196px, var(--berry) 402px,
      var(--white) 402px, var(--white) 492px,
      var(--mint) 492px, var(--mint) 1200px);
  }
  .band {
    position: absolute;
    display: flex;
    align-items: center;
    justify-content: center;
    white-space: nowrap;
  }
  .band-top {
    left: 150px;
    top: 196px;
    width: 452px;
    height: 206px;
    align-items: flex-end;
  }
  .band-middle {
    left: 150px;
    top: 402px;
    width: 452px;
    height: 90px;
  }
  .band-main {
    left: 0;
    top: 534px;
    width: 752px;
    height: 288px;
    background: var(--berry);
  }
  .stitch {
    position: absolute;
    left: 0;
    width: 752px;
    height: 0;
    border-top: 2px dashed var(--white);
  }
  .stitch-top { top: 20px; }
  .stitch-bottom { bottom: 20px; }
  .title-line {
    font-family: var(--title-font);
    font-weight: 200;
    line-height: 1;
    margin: 0;
  }
  .title-bright {
    color: var(--white);
    font-size: 112px;
    letter-spacing: -2px;
    padding-bottom: 12px;
  }
  .title-morning {
    color: var(--berry);
    font-size: 82px;
    font-weight: 300;
    letter-spacing: -1px;
  }
  .title-plan {
    color: var(--white);
    font-size: 262px;
    letter-spacing: -4px;
    margin-top: 6px;
  }
  .author {
    position: absolute;
    left: 0;
    top: 1114px;
    width: 752px;
    text-align: center;
    font-family: var(--author-font);
    font-weight: 700;
    font-size: 34px;
    line-height: 40px;
    color: var(--berry);
    letter-spacing: 0.5px;
    margin: 0;
  }
</style>
</head>
<body>
  <main class="cover">
    <div class="figure-area" role="img" aria-label="Flat silhouette of a woman's torso in a strapless berry top and mint skirt"></div>

    <div class="band band-top">
      <h1 class="title-line title-bright">BRIGHT</h1>
    </div>
    <div class="band band-middle">
      <p class="title-line title-morning">MORNING</p>
    </div>
    <div class="band band-main">
      <span class="stitch stitch-top"></span>
      <p class="title-line title-plan">PLAN</p>
      <span class="stitch stitch-bottom"></span>
    </div>

    <p class="author">MARISOL PENHALE</p>
  </main>
</body>
</html>
```